Morvik Construction Business Card

I need a business card design for my company.
We are a construction/machinery company.
I would like to see my logo on the front of the card and my details on the other side
I would like the card to be black or dark grey in colour,with my logo as i send it or modified with a lighter blue colour
I would like to see the design kept fairly simple,but eye catching at the same time
Industry/Entity Type
Business
Colors
00a990
1b1b1b
000000
474747
ececec

```html
<!DOCTYPE html>
<html lang="en">
<head>
<meta charset="utf-8">
<title>Morvik Construction – Business Card</title>
<link rel="stylesheet" href="https://fonts.googleapis.com/css2?family=Inter:wght@400;500&family=Michroma&display=swap">
<style>
  :root {
    --teal: #00a990;
    --ink: #000000;
    --charcoal: #1b1b1b;
    --grey: #474747;
    --paper: #ececec;
    --forest: #0b3a2c;
  }
  * { margin: 0; padding: 0; box-sizing: border-box; }
  html, body {
    width: 1200px;
    height: 1200px;
    overflow: hidden;
    background: var(--grey);
  }
  .sheet {
    width: 1200px;
    height: 1200px;
    display: flex;
    flex-direction: column;
    align-items: center;
    justify-content: center;
    gap: 50px;
  }
  .card {
    position: relative;
    width: 880px;
    height: 503px;
    border-radius: 12px;
    overflow: hidden;
    background: var(--ink);
    box-shadow: 0 10px 30px rgba(0,0,0,0.35);
  }

  /* Front */
  .card-front {
    display: flex;
    align-items: center;
    justify-content: center;
  }
  .brand-lockup {
    display: flex;
    align-items: center;
    gap: 24px;
  }
  .brand-mark {
    width: 64px;
    height: 64px;
    background: var(--paper);
    flex: none;
  }
  .brand-name {
    font-family: "Michroma", sans-serif;
    font-weight: 400;
    font-size: 52px;
    line-height: 1.15;
    color: var(--paper);
    letter-spacing: 1px;
    text-transform: uppercase;
  }

  /* Back */
  .card-back {
    background:
      radial-gradient(ellipse at 62% 50%, rgba(11,58,44,0.95) 0%, rgba(11,58,44,0.55) 40%, rgba(0,0,0,0) 72%),
      var(--ink);
  }
  .contact {
    position: absolute;
    left: 58px;
    top: 44px;
    font-family: "Inter", sans-serif;
    color: var(--paper);
  }
  .contact-name {
    font-size: 46px;
    font-weight: 400;
    letter-spacing: 0.5px;
  }
  .contact-role {
    font-size: 20px;
    font-weight: 400;
    margin-top: 2px;
  }
  .contact-list {
    list-style: none;
    margin-top: 34px;
    font-size: 22px;
    line-height: 44px;
  }
  .hazard-band {
    position: absolute;
    left: 0;
    right: 40px;
    bottom: 10px;
    height: 84px;
    background: linear-gradient(90deg, var(--teal) 0%, rgba(0,169,144,0.75) 55%, rgba(0,169,144,0.35) 92%, rgba(0,169,144,0) 100%);
  }
  .card-back .brand-lockup {
    position: absolute;
    right: 44px;
    top: 70px;
    gap: 8px;
  }
  .card-back .brand-mark {
    width: 16px;
    height: 16px;
  }
  .card-back .brand-name {
    font-size: 14px;
    letter-spacing: 0.5px;
  }
</style>
</head>
<body>
<main class="sheet">
  <section class="card card-front" aria-label="Card front">
    <div class="brand-lockup">
      <span class="brand-mark" aria-hidden="true"></span>
      <span class="brand-name">Morvik<br>Construction</span>
    </div>
  </section>

  <section class="card card-back" aria-label="Card back">
    <div class="contact">
      <h1 class="contact-name">Evan Marlow</h1>
      <p class="contact-role">Sales Advisor</p>
      <ul class="contact-list">
        <li>Address&nbsp; -</li>
        <li>Phone -</li>
        <li>Email&nbsp; -</li>
      </ul>
    </div>
    <div class="hazard-band" role="img" aria-label="Teal diagonal hazard-stripe band along the lower edge"></div>
    <div class="brand-lockup">
      <span class="brand-mark" aria-hidden="true"></span>
      <span class="brand-name">Morvik<br>Construction</span>
    </div>
  </section>
</main>
</body>
</html>
```